Small consulting business needs logo and business card design

I need a logo, business card and letterhead design for a small consulting firm called Veltramo Consulting. My customers are generally small to medium sized businesses but I have done work for major corporates and government departments. The field of consulting is strategic/business planning and program management. I have blue as the predominate colour in my current business card but I am happy to change this for the right design
Industry/Entity Type
Business

```html
<!DOCTYPE html>
<html lang="en">
<head>
<meta charset="utf-8">
<title>Veltramo Consulting – Business Card</title>
<link rel="stylesheet" href="https://fonts.googleapis.com/css2?family=Exo+2:wght@400;500;700&display=swap">
<style>
  :root {
    --page: #e9e6e1;
    --card-dark: #343434;
    --blue-light: #8fc0ec;
    --blue: #4d8fd0;
    --silver-light: #f2f2f2;
    --silver: #a9a9a9;
    --text: #ffffff;
    --text-soft: #e6e6e6;
  }
  * { margin: 0; padding: 0; box-sizing: border-box; }
  html, body { width: 1200px; height: 899px; overflow: hidden; background: var(--page); }
  body { position: relative; font-family: "Exo 2", sans-serif; color: var(--text); }

  .card {
    position: absolute;
    left: 280px;
    width: 640px;
    height: 366px;
    overflow: hidden;
    box-shadow: 0 6px 18px rgba(0,0,0,.25);
  }
  .card--front { top: 66px; }
  .card--back { top: 466px; }
  .card__art { position: absolute; inset: 0; width: 100%; height: 100%; }

  .wordmark { position: absolute; font-weight: 700; color: var(--text); line-height: 1.05; }
  .wordmark__line { display: block; }
  .card--front .wordmark { left: 150px; top: 100px; font-size: 50px; letter-spacing: 1px; }
  .card--back .wordmark { left: 372px; top: 118px; font-size: 40px; letter-spacing: 1px; }

  .front__web {
    position: absolute; left: 190px; top: 300px;
    font-size: 15px; letter-spacing: 3px; color: var(--text-soft);
  }

  .divider {
    position: absolute; left: 340px; top: 60px;
    width: 2px; height: 230px; background: #d9d9d9;
  }
  .person { position: absolute; left: 60px; top: 66px; }
  .person__name { font-size: 17px; font-weight: 500; letter-spacing: 1px; }
  .person__role { font-size: 13px; color: var(--text-soft); margin-left: 4px; }
  .address { position: absolute; left: 78px; top: 150px; font-size: 13px; line-height: 1.45; color: var(--text-soft); letter-spacing: .5px; }

  .contacts { position: absolute; left: 92px; top: 232px; list-style: none; font-size: 11px; color: var(--text-soft); letter-spacing: .8px; }
  .contacts li { display: flex; align-items: center; height: 19px; }
  .contacts svg { width: 11px; height: 11px; margin-right: 8px; fill: var(--text-soft); }
</style>
</head>
<body>

<section class="card card--front" aria-label="Business card front">
  <svg class="card__art" viewBox="0 0 640 366" aria-hidden="true">
    <defs>
      <linearGradient id="blueSweep" x1="0" y1="0" x2="1" y2="1">
        <stop offset="0" stop-color="var(--blue-light)"/>
        <stop offset="1" stop-color="var(--blue)"/>
      </linearGradient>
      <linearGradient id="silverSweep" x1="0" y1="0" x2="1" y2="1">
        <stop offset="0" stop-color="var(--silver-light)"/>
        <stop offset="1" stop-color="var(--silver)"/>
      </linearGradient>
    </defs>
    <rect width="640" height="366" fill="var(--card-dark)"/>
    <path d="M0 0 H340 L0 250 Z" fill="url(#blueSweep)"/>
    <path d="M0 200 L300 366 H0 Z" fill="url(#silverSweep)"/>
    <path d="M640 110 V366 H330 Z" fill="url(#silverSweep)"/>
    <ellipse cx="335" cy="165" rx="315" ry="200" transform="rotate(-8 335 165)" fill="var(--card-dark)"/>
  </svg>
  <h1 class="wordmark">
    <span class="wordmark__line">VELTRAMO</span>
    <span class="wordmark__line">Consulting</span>
  </h1>
  <p class="front__web">www.veltramo.com</p>
</section>

<section class="card card--back" aria-label="Business card back">
  <svg class="card__art" viewBox="0 0 640 366" aria-hidden="true">
    <defs>
      <linearGradient id="blueSweepBack" x1="0" y1="0" x2="1" y2="1">
        <stop offset="0" stop-color="var(--blue-light)"/>
        <stop offset="1" stop-color="var(--blue)"/>
      </linearGradient>
      <linearGradient id="silverSweepBack" x1="0" y1="0" x2="1" y2="1">
        <stop offset="0" stop-color="var(--silver-light)"/>
        <stop offset="1" stop-color="var(--silver)"/>
      </linearGradient>
    </defs>
    <rect width="640" height="366" fill="var(--card-dark)"/>
    <path d="M280 0 H640 V260 Z" fill="url(#blueSweepBack)"/>
    <path d="M640 200 V366 H380 Z" fill="url(#silverSweepBack)"/>
    <path d="M0 220 L260 366 H0 Z" fill="url(#silverSweepBack)"/>
    <ellipse cx="300" cy="195" rx="320" ry="190" transform="rotate(4 300 195)" fill="var(--card-dark)"/>
  </svg>

  <div class="person">
    <p class="person__name">DANIEL MORROW</p>
    <p class="person__role">Managing Director</p>
  </div>
  <p class="address">041.12th floor.Harbour<br>Crest Road NVK</p>

  <ul class="contacts">
    <li><svg viewBox="0 0 12 12"><path d="M2.5 1 4.5 3.3 3.6 4.6Q4.8 7 7.3 8.4L8.7 7.5 11 9.5 9.8 11Q5.5 10.7 1 2.3Z"/></svg>012 555 0147</li>
    <li><svg viewBox="0 0 12 12"><path d="M3 0H9V12H3ZM4 1.5V9.5H8V1.5Z"/></svg>012 555 0148</li>
    <li><svg viewBox="0 0 12 12"><path d="M3 0H9V3H3ZM1 4H11V9H9V12H3V9H1ZM4 8V11H8V8Z"/></svg>012 555 0149</li>
    <li><svg viewBox="0 0 12 12"><path d="M0 2H12V10H0ZM1 3 6 7 11 3Z"/></svg>hello@veltramo.com</li>
    <li><svg viewBox="0 0 12 12"><circle cx="6" cy="6" r="5.5"/><path d="M0.5 6H11.5M6 0.5V11.5M2 3H10M2 9H10" stroke="var(--card-dark)" stroke-width="0.8"/></svg>www.veltramo.com</li>
  </ul>

  <span class="divider" aria-hidden="true"></span>

  <h2 class="wordmark">
    <span class="wordmark__line">VELTRAMO</span>
    <span class="wordmark__line">Consulting</span>
  </h2>
</section>

</body>
</html>
```